Driver License Monitoring Application Marketing Website

We need a new web design for our web application. The product is called "PermitSentry." We provide a driver license monitoring service to companies and local government bodies with driver fleets. Our current website is available at www.PermitSentry-demo.net.

I prefer a clean, single-page design with good SEO. Attached are some PDFs with data about the project.

Target Market(s)

Companies with driver fleets, local government.

Industry/Entity Type

Government

Coding

Coded - Design and coding required

Number of Pages Required

1 page

Colors
000000

Requirements
Must have
• Content from current www.PermitSentry-demo.net and attached PDFs.
Nice to have
• Prefer a simple Bootstrap or similar design for easy editing.
• Room for a simple video explanation of how the product works (we don't have an actual video yet)

```html
<!DOCTYPE html>
<html lang="en">
<head>
<meta charset="utf-8">
<title>PermitSentry – Florida Driver License Monitoring Service</title>
<link rel="stylesheet" href="https://fonts.googleapis.com/css2?family=Source+Sans+3:wght@300;400;600;700&family=Open+Sans:wght@400;600&family=Roboto+Condensed:wght@700&display=swap">
<style>
  :root {
    --ink: #333a40;
    --muted: #8c8c8c;
    --white: #ffffff;
    --section-alt: #f7f7f7;
    --accent-red: #b3161d;
    --rule: #d6d6d6;
    --hero-dark: #2a2426;
    --hero-mid: #4a3a3c;
    --copy: #5e5e5e;
  }
  * { box-sizing: border-box; }
  html, body { margin: 0; padding: 0; }
  body {
    width: 725px;
    height: 1200px;
    overflow: hidden;
    position: relative;
    background: var(--white);
    font-family: "Open Sans", Arial, sans-serif;
    color: var(--ink);
  }

  /* Hero */
  .hero {
    position: absolute; left: 0; top: 0;
    width: 725px; height: 285px;
    background: linear-gradient(100deg, #9a9a9c 0%, #6d6567 18%, var(--hero-mid) 38%, var(--hero-dark) 70%, #1e1a1c 100%);
  }
  .hero-eyebrow {
    position: absolute; top: 35px; left: 0; width: 100%;
    text-align: center; margin: 0;
    font-family: "Source Sans 3", "Source Sans Pro", Arial, sans-serif;
    font-size: 12px; font-weight: 400; color: var(--white);
  }
  .hero-title {
    position: absolute; top: 57px; left: 0; width: 100%;
    text-align: center; margin: 0;
    font-family: "Source Sans 3", "Source Sans Pro", Arial, sans-serif;
    font-weight: 300; font-size: 29px; line-height: 34px;
    letter-spacing: -1.3px; color: var(--white);
  }
  .product-screens {
    position: absolute; left: 207px; top: 155px;
    width: 311px; height: 190px;
    border-radius: 6px;
    background: linear-gradient(180deg, #e9e9ea 0%, #cfd0d2 100%);
    box-shadow: 0 8px 14px rgba(0,0,0,.15);
  }

  /* Section headings */
  .section-title {
    position: absolute; left: 0; width: 100%; margin: 0;
    text-align: center;
    font-family: "Source Sans 3", "Source Sans Pro", Arial, sans-serif;
    font-weight: 700; font-size: 21px; line-height: 26px; letter-spacing: -1px;
    color: var(--ink);
  }
  .section-rule {
    position: absolute; left: 330px; width: 66px; height: 1px;
    background: var(--rule);
  }

  /* Features */
  .feature { position: absolute; width: 150px; }
  .feature-title {
    margin: 0 0 5px;
    display: flex; align-items: center; gap: 6px;
    font-size: 10.5px; line-height: 14px; font-weight: 600; color: var(--ink);
  }
  .feature-title svg { width: 12px; height: 12px; fill: var(--ink); flex: none; }
  .feature-text {
    margin: 0;
    font-size: 8.2px; line-height: 12.8px; letter-spacing: .2px;
    color: var(--muted);
  }

  /* Stats */
  .stats {
    position: absolute; left: 0; top: 755px;
    width: 725px; height: 445px;
    background: var(--section-alt);
  }
  .truck {
    position: absolute; left: 155px; top: 945px;
    width: 251px; height: 112px;
    background: linear-gradient(90deg, #e4e4e4 0%, #f3f3f3 70%, #c0262b 78%, #a51a20 100%);
    border-radius: 3px;
  }
  .stat-badge {
    position: absolute; width: 44px; height: 44px; border-radius: 50%;
    background: var(--accent-red); color: var(--white);
    display: flex; align-items: center; justify-content: center;
    font-family: "Roboto Condensed", Arial, sans-serif; font-weight: 700; font-size: 13px;
  }
  .stat-label {
    position: absolute; margin: 0;
    font-family: "Roboto Condensed", Arial, sans-serif; font-weight: 700;
    font-size: 10px; line-height: 12px; color: #111;
    padding-bottom: 3px; border-bottom: 1px solid #555;
    width: 112px;
  }
  .stat-lines { position: absolute; left: 0; top: 0; width: 725px; height: 1200px; pointer-events: none; }
  .stats-copy {
    position: absolute; left: 70px; top: 1076px; width: 585px; margin: 0;
    text-align: center;
    font-family: "Source Sans 3", "Source Sans Pro", Arial, sans-serif; font-weight: 300;
    font-size: 12.5px; line-height: 18.5px; color: var(--copy);
  }
</style>
</head>
<body>

<header class="hero" role="img" aria-label="Photograph of a white truck cab viewed from above on a dark road">
  <p class="hero-eyebrow">Florida Driver License Monitoring Service</p>
  <h1 class="hero-title">How many of your drivers currently have<br>a suspended license?</h1>
</header>
<div class="product-screens" role="img" aria-label="PermitSentry dashboard shown on a desktop monitor and a laptop"></div>

<section class="features">
  <h2 class="section-title" style="top:418px;">Monitor your Whole Fleet Online</h2>
  <div class="section-rule" style="top:450px;"></div>

  <article class="feature" style="left:121px; top:499px;">
    <h3 class="feature-title"><svg viewBox="0 0 12 12"><path d="M2 1l9 3-4 1-1 6z"/></svg>Some Feature</h3>
    <p class="feature-text">Messenger bag gentrify pitchfork tattooed craft beer, laptop skateboard locavore cardigan artisan vinyl craft beer blog stumptown salvia mural cred.</p>
  </article>
  <article class="feature" style="left:288px; top:499px;">
    <h3 class="feature-title"><svg viewBox="0 0 12 12"><ellipse cx="6" cy="2.5" rx="5" ry="2"/><path d="M1 4c0 1.1 2.2 2 5 2s5-.9 5-2v2c0 1.1-2.2 2-5 2S1 7.1 1 6zM1 7.5c0 1.1 2.2 2 5 2s5-.9 5-2v2c0 1.1-2.2 2-5 2s-5-.9-5-2z"/></svg>Another amazing feature</h3>
    <p class="feature-text">Messenger bag gentrify pitchfork tattooed craft beer, laptop skateboard locavore cardigan artisan vinyl craft beer blog stumptown salvia mural cred.</p>
  </article>
  <article class="feature" style="left:455px; top:499px;">
    <h3 class="feature-title"><svg viewBox="0 0 12 12"><path d="M11 0L5 7l1 1 6-7zM4 8c-2 0-2 2-4 3 3 1 5 0 5-2z"/></svg>Feature title</h3>
    <p class="feature-text">Messenger bag gentrify pitchfork tattooed craft beer, laptop skateboard locavore cardigan artisan vinyl craft beer blog stumptown salvia mural cred.</p>
  </article>

  <article class="feature" style="left:121px; top:616px;">
    <h3 class="feature-title"><svg viewBox="0 0 12 12"><path d="M0 2h12v1.5L6 7 0 3.5zM0 5l6 3.5L12 5v5H0z"/></svg>Important feature</h3>
    <p class="feature-text">Messenger bag gentrify pitchfork tattooed craft beer, laptop skateboard locavore cardigan artisan vinyl craft beer blog stumptown salvia mural cred.</p>
  </article>
  <article class="feature" style="left:288px; top:616px;">
    <h3 class="feature-title"><svg viewBox="0 0 12 12"><path d="M0 4h3l7-3v10L3 8H0zM3 8l1 3h2L5 8z"/></svg>Amazing feature</h3>
    <p class="feature-text">Messenger bag gentrify pitchfork tattooed craft beer, laptop skateboard locavore cardigan artisan vinyl craft beer blog stumptown salvia mural cred.</p>
  </article>
  <article class="feature" style="left:455px; top:616px;">
    <h3 class="feature-title"><svg viewBox="0 0 12 12"><path d="M0 2h12v8H0zm1 1v6h10V3zm1 1h3v3H2zm4 0h4v1H6zm0 2h4v1H6z" fill-rule="evenodd"/></svg>Epic title goes here</h3>
    <p class="feature-text">Messenger bag gentrify pitchfork tattooed craft beer, laptop skateboard locavore cardigan artisan vinyl craft beer blog stumptown salvia mural cred.</p>
  </article>
</section>

<section class="stats"></section>
<h2 class="section-title" style="top:817px;">Monitor your Whole Fleet Online</h2>
<div class="section-rule" style="top:848px;"></div>

<div class="truck" role="img" aria-label="Illustration of a red and white semi truck with the trailer reading 1 of every 10 drivers have a suspended license"></div>

<svg class="stat-lines" viewBox="0 0 725 1200" aria-hidden="true">
  <line x1="210" y1="918" x2="180" y2="950" stroke="#333" stroke-width="1"/>
</svg>

<div class="stat-badge" style="left:201px; top:879px;">12%</div>
<p class="stat-label" style="left:251px; top:890px;">SUSPENSIONS PER YEAR!</p>

<div class="stat-badge" style="left:345px; top:912px;">1.8</div>
<p class="stat-label" style="left:395px; top:923px;">MILLION SUSPENSIONS</p>

<div class="stat-badge" style="left:407px; top:980px;">100%</div>
<p class="stat-label" style="left:455px; top:988px; width:110px; padding-left:12px;">15 MILLION DRIVERS</p>

<p class="stats-copy">How many of your drivers currently have a suspended license? The answer may suspise you. Drivind with a suspended license is the most commonly committed offense in America. In 2011, over 1.8 million licenses got suspended in Florida. With just over 15 million drivers, tha's 12% of all licensed Florida drivers.</p>

</body>
</html>
```